Retirement Plan Advisor Bio

See the attached document and photo for content. I would like someone to design this one page flyer using my logo. This logo was designed by a designer with sketch hive. I am looking for a professional looking document. I want to he color scheme to be primarily white and gold.

Target Market(s)

Employers who offer a retirement plan

Requirements
Should not have
• The designs that I have received look more like resumes. I am interested in advertising my Retirement plan services. If anyone can change their submissions and change it to an ad for retirement plan services instead of a Bio or resume, I would prefer that.

```html
<!DOCTYPE html>
<html lang="en">
<head>
<meta charset="utf-8">
<title>Retirement Plan Advisor – Helen S Dawes</title>
<link rel="stylesheet" href="https://fonts.googleapis.com/css2?family=Lato:wght@400;700&family=Roboto:wght@300;400&display=swap">
<style>
  :root {
    --page-bg: #e9e9e9;
    --paper: #ffffff;
    --gold-light: #f0cf8c;
    --gold: #dcae5c;
    --gold-deep: #c88d2a;
    --ink: #5e5e5e;
    --ink-dark: #2f2f2f;
    --bullet: #a9a9a9;
    --band-grey: #b3b3b3;
    --white: #ffffff;
  }
  * { box-sizing: border-box; margin: 0; padding: 0; }
  html, body { width: 768px; height: 1200px; overflow: hidden; background: var(--page-bg); }
  .stage { position: relative; width: 768px; height: 1200px; }
  .flyer {
    position: absolute; left: 111px; top: 17px;
    width: 757px; height: 1620px;
    transform: scale(0.72); transform-origin: 0 0;
    background: var(--paper);
    font-family: "Lato", sans-serif;
    color: var(--ink);
    overflow: hidden;
  }
  .brand-band {
    position: absolute; left: 0; top: 155px; width: 757px; height: 135px;
    background: linear-gradient(90deg, var(--gold-deep) 0%, var(--gold-light) 25%, var(--gold) 55%, var(--gold-deep) 85%, var(--gold-light) 100%);
    box-shadow: 0 10px 10px -6px rgba(0,0,0,.25);
  }
  .brand {
    position: absolute; left: 60px; top: 202px;
    display: flex; align-items: center; gap: 14px;
    font-family: "Lato", sans-serif; font-weight: 700; font-size: 28px; color: var(--white);
  }
  .brand-mark { width: 34px; height: 34px; background: var(--white); }
  .portrait-ring {
    position: absolute; left: 382px; top: 29px; width: 356px; height: 356px; border-radius: 50%;
    background: linear-gradient(150deg, var(--gold-deep), var(--gold-light) 45%, var(--gold-deep));
    box-shadow: 0 4px 10px rgba(0,0,0,.25);
  }
  .portrait {
    position: absolute; left: 15px; top: 15px; width: 326px; height: 326px; border-radius: 50%;
    background: radial-gradient(circle at 50% 45%, #d9c59a 0%, #a9a6a3 40%, #6f86a8 75%, #4f6688 100%);
  }
  .headline { position: absolute; left: 84px; top: 372px; font-size: 39px; font-weight: 400; color: var(--ink); }
  .intro { position: absolute; left: 84px; top: 428px; width: 620px; font-size: 26px; line-height: 32.6px; color: var(--ink); }
  .section-band {
    position: absolute; left: 0; width: 455px; height: 46px;
    clip-path: polygon(0 0, 443px 0, 455px 46px, 0 46px);
    padding-left: 83px; line-height: 47px;
    font-size: 24px; color: var(--white); letter-spacing: .2px;
    background: linear-gradient(90deg, var(--gold-light), var(--gold) 50%, var(--gold-light));
  }
  .section-band.muted { background: var(--band-grey); }
  .band-shadow { position: absolute; left: 0; width: 455px; height: 8px; background: linear-gradient(rgba(0,0,0,.12), rgba(0,0,0,0)); }
  .bullets { position: absolute; left: 84px; width: 590px; list-style: none; font-family: "Roboto", sans-serif; font-weight: 300; font-size: 23px; line-height: 29.5px; color: var(--ink-dark); }
  .bullets li { position: relative; padding-left: 21px; margin-bottom: 5px; }
  .bullets li::before { content: ""; position: absolute; left: 0; top: 10px; width: 12px; height: 12px; border-radius: 50%; background: var(--bullet); }
  .bullets .tight { line-height: 21px; }
  .signature-line {
    position: absolute; left: 716px; top: 1470px; transform: rotate(-90deg); transform-origin: 0 0;
    font-size: 14px; color: #bdbdbd; white-space: nowrap;
  }
  .contact-band {
    position: absolute; left: 0; top: 1493px; width: 757px; height: 127px;
    background: linear-gradient(90deg, var(--gold-light) 0%, var(--gold) 40%, var(--gold-deep) 60%, var(--gold-light) 100%);
    box-shadow: 0 -8px 10px -6px rgba(0,0,0,.2);
  }
  .contact { position: absolute; top: 26px; font-size: 22px; line-height: 26px; color: var(--white); }
  .contact.left { left: 86px; }
  .contact.right { left: 447px; }
</style>
</head>
<body>
<div class="stage">
  <div class="flyer">
    <div class="brand-band"></div>
    <div class="brand"><span class="brand-mark"></span>Verano Financial, LLC</div>
    <div class="portrait-ring"><div class="portrait" role="img" aria-label="Portrait photo of the advisor"></div></div>

    <h1 class="headline">I strive to improve</h1>
    <p class="intro">retirement outcomes for my plan sponsor clients and their employees through careful retirement plan design assistance, strategic and targeted communication and education, as well as continual monitoring of results.</p>

    <div class="section-band" style="top:632px">PROFESSIONAL SPECIALTIES</div>
    <div class="band-shadow" style="top:678px"></div>
    <ul class="bullets" style="top:689px">
      <li>Over 18 years of experience in the retirement plan industry</li>
      <li>Focused on helping plan sponsors reduce administrative burdens and fiduciary risk</li>
      <li>Dedicated to helping employees work toward a positive retirement outcome through careful analysis of their savings rate , investment strategy and overall financial wellness</li>
    </ul>

    <div class="section-band" style="top:973px">QUALIFICATIONS</div>
    <div class="band-shadow" style="top:1019px"></div>
    <ul class="bullets" style="top:1033px">
      <li>Certified Financial Planner®</li>
      <li>Accredited Investment Fiduciary®</li>
      <li class="tight">Investment Advisor Representative<br>Series 7, 63, and 65 Securities licenses with Northgate Financial</li>
      <li>Holds Life and Health Insurance licenses from Illinois</li>
    </ul>

    <div class="section-band muted" style="top:1240px">EDUCATION</div>
    <div class="band-shadow" style="top:1286px"></div>
    <ul class="bullets" style="top:1300px">
      <li>BS Halden University, 1987</li>
      <li>Securities and Investment Advisory Services offered through Northgate Financial Holdings, Inc, a Registered Broker/Dealer and In-<br>vestment Advisor, member NSRA/IPSC</li>
    </ul>

    <div class="signature-line">Helen S Dawes CFP®AIF®</div>

    <div class="contact-band">
      <p class="contact left">Northgate Financial Advisor 2400<br>Springvale, IL 60000<br>helen.dawes@northgatefin.com</p>
      <p class="contact right">Marlow Rd.<br>(555)010.4821<br>Www.helendawes.com</p>
    </div>
  </div>
</div>
</body>
</html>
```